Start up in business consultancy needs a business card

We need the business card's layout (we have already the logo). Our business is concerned on consultancy services delivered to companies on the matter of sustainability. Business card should be enough essentials and professional style.

Side A with the following info:
logo + a space for the claim (still to identify) + website of the company

Side B with the following info:
Name of business card holder + title of the business card holder + address of the company + space for mobile number, phone number, fax number + e-mail of business card holder + graphic details around.

Target Market(s)

Business of any sector

Industry/Entity Type

Business Service

Contact Information for Business Card

Name of the company:
Lumeroca srl
Società Benefit

Address of the company:
Via Pescoli, 7
21099 - Castelmirano (CM)

Website:
www.lumeroca-esempio.it

Name of the BC' holder:
Ettore Valsenzi

Title:
Co-fondatore

Email:
ettore@lumeroca-esempio.it

Mobile:
+39 351 602 7415
Phone:
+39 351 602 7415
Fax:
+39 351 602 7415

Font styles to use
Other font styles liked:
• new gothic

```html
<!DOCTYPE html>
<html lang="it">
<head>
<meta charset="utf-8">
<title>Lumeroca – biglietto da visita</title>
<link rel="stylesheet" href="https://fonts.googleapis.com/css2?family=Roboto+Condensed:wght@300;400;700&display=swap">
<style>
  :root {
    --brand-blue: #0a7cc1;
    --brand-blue-deep: #0862a3;
    --band-grey: #a6a7a9;
    --card-white: #f7f7f7;
    --ink-white: #ffffff;
    --stage: #e8e6e1;
  }
  * { margin: 0; padding: 0; box-sizing: border-box; }
  html, body { width: 1200px; height: 780px; overflow: hidden; background: var(--stage); }
  body { font-family: "Roboto Condensed", "Arial Narrow", sans-serif; }

  .canvas { position: relative; width: 1200px; height: 780px; }

  .card {
    position: absolute;
    top: 232px;
    width: 540px;
    height: 315px;
    overflow: hidden;
    box-shadow: 0 6px 18px rgba(0,0,0,0.18);
  }

  /* Info side */
  .card--info { left: 40px; background: var(--card-white); }
  .card--info .band-grey {
    position: absolute; left: 0; right: 0; top: 146px; height: 62px;
    background: var(--band-grey);
  }
  .card--info .band-blue {
    position: absolute; left: 0; right: 0; top: 208px; bottom: 0;
    background: var(--brand-blue);
  }
  .card--info .accent-ring {
    position: absolute; left: 396px; top: 14px; width: 206px; height: 206px;
  }
  .brand-lockup {
    position: absolute; left: 34px; top: 68px;
    display: flex; align-items: center; gap: 14px;
  }
  .brand-lockup .mark { width: 62px; height: 62px; }
  .brand-name {
    font-weight: 400; font-size: 42px; letter-spacing: 0.5px;
    color: var(--brand-blue); line-height: 1;
  }
  .company-block {
    position: absolute; left: 34px; top: 152px;
    color: var(--ink-white); font-weight: 300; font-size: 14px; line-height: 17px;
  }
  .company-block b { font-weight: 700; }
  .holder-block {
    position: absolute; left: 34px; top: 218px;
    color: var(--ink-white); font-size: 15px; line-height: 20px; font-weight: 300;
  }
  .holder-name { font-weight: 700; font-size: 21px; line-height: 26px; }
  .holder-title { font-weight: 300; font-size: 17px; }
  .holder-block b { font-weight: 700; }

  /* Brand side */
  .card--brand {
    left: 620px;
    background: radial-gradient(ellipse at 45% 40%, #1593d4 0%, var(--brand-blue) 45%, var(--brand-blue-deep) 100%);
  }
  .card--brand .brand-lockup { left: 118px; top: 104px; }
  .card--brand .brand-name { color: var(--ink-white); font-size: 46px; }
  .card--brand .mark { width: 72px; height: 72px; }
  .website {
    position: absolute; left: 118px; top: 196px;
    color: var(--ink-white); font-size: 15px; font-weight: 400; letter-spacing: 0.3px;
  }
</style>
</head>
<body>
<main class="canvas">

  <section class="card card--info" aria-label="Fronte con contatti">
    <div class="band-grey"></div>
    <div class="band-blue"></div>
    <svg class="accent-ring" viewBox="0 0 206 206" aria-hidden="true">
      <circle cx="103" cy="103" r="99" fill="var(--card-white)" stroke="var(--brand-blue)" stroke-width="5"/>
    </svg>

    <div class="brand-lockup">
      <svg class="mark" viewBox="0 0 62 62" aria-hidden="true">
        <circle cx="31" cy="31" r="28" fill="none" stroke="var(--brand-blue)" stroke-width="3.5"/>
      </svg>
      <span class="brand-name">lumeroca</span>
    </div>

    <div class="company-block">
      <p>Lumeroca Società Benefit srl</p>
      <p>Via Pescoli, 7</p>
      <p>21099 - Castelmirano (CM) &nbsp;|&nbsp; <b>P.IVA/CF:</b> 04826150937</p>
    </div>

    <div class="holder-block">
      <p><span class="holder-name">Ettore Valsenzi</span> <span class="holder-title">| Co-fondatore</span></p>
      <p><b>M:</b> +39 351 602 7415 &nbsp;|&nbsp; <b>F:</b> +39 351 602 7415</p>
      <p><b>E:</b> ettore@lumeroca-esempio.it</p>
    </div>
  </section>

  <section class="card card--brand" aria-label="Retro con marchio">
    <div class="brand-lockup">
      <svg class="mark" viewBox="0 0 72 72" aria-hidden="true">
        <circle cx="36" cy="36" r="32" fill="none" stroke="var(--ink-white)" stroke-width="4"/>
      </svg>
      <span class="brand-name">lumeroca</span>
    </div>
    <p class="website">www.lumeroca-esempio.it</p>
  </section>

</main>
</body>
</html>
```